Automotive Accessories Business Card

Design a business template that match our new logo design and our industry.

https://www.kelvorauto.com/

Target Market(s)

Aftermarket auto parts and accessories

Industry/Entity Type

automotive

Contact Information for Business Card

company logo

Font styles to use
Serif
Sans Serif

Colors
EB3D1F
EC4F4E
F09395
F8D3D4
FCEDEE

```html
<!DOCTYPE html>
<html lang="en">
<head>
<meta charset="utf-8">
<title>Kelvor Auto – Business Card</title>
<link href="https://fonts.googleapis.com/css2?family=Poppins:wght@400;500;600;700&display=swap" rel="stylesheet">
<style>
  :root {
    --red: #EB3D1F;
    --red-card: #EC2A2E;
    --red-soft: #EC4F4E;
    --pink: #F09395;
    --pink-light: #F8D3D4;
    --blush: #FCEDEE;
    --ink: #3a3a3a;
    --stage: #ededed;
    --white: #ffffff;
  }
  * { box-sizing: border-box; margin: 0; padding: 0; }
  html, body {
    width: 1200px; height: 800px; overflow: hidden;
    background: var(--stage);
    font-family: "Poppins", sans-serif;
  }
  .sheet {
    width: 1200px; height: 800px;
    display: flex; flex-direction: column;
    align-items: center; justify-content: center; gap: 40px;
  }
  .card {
    width: 560px; height: 320px;
    border-radius: 26px;
    position: relative;
    overflow: hidden;
    box-shadow: 0 6px 18px rgba(0,0,0,0.12);
  }

  /* Front */
  .card--front { background: var(--red-card); }
  .front__brand {
    position: absolute; left: 0; right: 0; top: 92px;
    display: flex; align-items: center; justify-content: center; gap: 16px;
  }
  .front__mark {
    width: 34px; height: 34px; background: var(--pink-light);
  }
  .front__name {
    font-weight: 700; font-size: 56px; letter-spacing: 2px;
    color: var(--pink-light); line-height: 1;
  }
  .front__tagline {
    position: absolute; left: 0; right: 0; bottom: 56px;
    text-align: center; font-size: 16px; font-weight: 500;
    color: var(--red-soft); filter: brightness(1.12);
    letter-spacing: 0.5px;
  }

  /* Back */
  .card--back { background: var(--white); }
  .back__person {
    position: absolute; left: 52px; top: 106px;
  }
  .back__name {
    font-weight: 600; font-size: 30px; color: var(--red); line-height: 1.1;
  }
  .back__role {
    font-size: 11px; letter-spacing: 0.6px; color: var(--ink); margin-top: 4px;
  }
  .back__divider {
    position: absolute; left: 290px; top: 56px;
    width: 2px; height: 170px; background: var(--red);
  }
  .back__contacts {
    position: absolute; left: 314px; top: 52px;
    list-style: none; font-size: 12.5px; color: var(--ink); line-height: 1.45;
  }
  .contact {
    display: flex; align-items: flex-start; gap: 12px; margin-bottom: 9px;
  }
  .contact svg { flex: none; width: 14px; height: 14px; margin-top: 2px; fill: var(--red); }
  .back__brand {
    position: absolute; left: 52px; bottom: 40px;
    display: flex; align-items: center; gap: 10px;
  }
  .back__mark { width: 18px; height: 18px; background: var(--red); }
  .back__brandname {
    font-weight: 700; font-size: 28px; letter-spacing: 1px; color: var(--ink); line-height: 1;
  }
</style>
</head>
<body>
<main class="sheet">
  <section class="card card--front" aria-label="Card front">
    <div class="front__brand">
      <span class="front__mark"></span>
      <span class="front__name">KELVOR AUTO</span>
    </div>
    <p class="front__tagline">Aftermarket auto parts and accessories</p>
  </section>

  <section class="card card--back" aria-label="Card back">
    <div class="back__person">
      <h1 class="back__name">Marcel Ostrand</h1>
      <p class="back__role">DIRECTEUR FONDATEUR</p>
    </div>
    <div class="back__divider"></div>
    <ul class="back__contacts">
      <li class="contact">
        <svg viewBox="0 0 24 24"><path d="M12 2a7 7 0 0 0-7 7c0 5 7 13 7 13s7-8 7-13a7 7 0 0 0-7-7zm0 9.5A2.5 2.5 0 1 1 12 6.5a2.5 2.5 0 0 1 0 5z"/></svg>
        <span>240 W. Harbor Ave. Unit B<br>Riverton, CA, 92880<br>United States</span>
      </li>
      <li class="contact">
        <svg viewBox="0 0 24 24"><path d="M12 2a10 10 0 1 0 0 20 10 10 0 0 0 0-20zm6.9 6h-3a15 15 0 0 0-1.3-3.9A8 8 0 0 1 18.9 8zM12 4c.8 1.2 1.5 2.5 1.9 4h-3.8c.4-1.5 1.1-2.8 1.9-4zM4.3 14a8 8 0 0 1 0-4h3.4a16 16 0 0 0 0 4zm.8 2h3a15 15 0 0 0 1.3 3.9A8 8 0 0 1 5.1 16zm3-8h-3a8 8 0 0 1 4.3-3.9A15 15 0 0 0 8.1 8zM12 20c-.8-1.2-1.5-2.5-1.9-4h3.8c-.4 1.5-1.1 2.8-1.9 4zm2.3-6H9.7a14 14 0 0 1 0-4h4.6a14 14 0 0 1 0 4zm.3 5.9a15 15 0 0 0 1.3-3.9h3a8 8 0 0 1-4.3 3.9zM16.3 14a16 16 0 0 0 0-4h3.4a8 8 0 0 1 0 4z"/></svg>
        <span>kelvorauto.com</span>
      </li>
      <li class="contact">
        <svg viewBox="0 0 24 24"><path d="M2 5h20v14H2zm2 2v.5l8 5 8-5V7z"/></svg>
        <span>sales@kelvorauto.com</span>
      </li>
      <li class="contact">
        <svg viewBox="0 0 24 24"><path d="M6.6 10.8a15 15 0 0 0 6.6 6.6l2.2-2.2a1 1 0 0 1 1-.25 11 11 0 0 0 3.6.6 1 1 0 0 1 1 1V20a1 1 0 0 1-1 1A17 17 0 0 1 3 4a1 1 0 0 1 1-1h3.5a1 1 0 0 1 1 1 11 11 0 0 0 .6 3.6 1 1 0 0 1-.25 1z"/></svg>
        <span>1.800.555.0148</span>
      </li>
    </ul>
    <div class="back__brand">
      <span class="back__mark"></span>
      <span class="back__brandname">KELVOR AUTO</span>
    </div>
  </section>
</main>
</body>
</html>
```